Gentleman's grooming products require a business card

I need a business card that incorporates the logo [ or parts of ] that we had Pixel Hive design for us as uploaded.

We sell online, mens grooming products including moustache waxes, beard oils and shaving accessories.
We want a card that is classy, professional and a card that shouts mens products.

Target Market(s)

Young professional male market

Industry/Entity Type

Business

Contact Information for Business Card

Ross and Edith Carwell
Lather and Lore
Purveyors of gentleman's stiffeners and grooming requisites
M :0418529647
E : ross@latherandlore.com.au
E : edith@latherandlore.com.au
E : sales@theblokesbalmery.com.au

W : www.latherandlore.com.au

Requirements
Must have
• Class
Nice to have
• Professionalism

```html
<!DOCTYPE html>
<html lang="en">
<head>
<meta charset="utf-8">
<title>Lather and Lore – Business Card</title>
<link rel="stylesheet" href="https://fonts.googleapis.com/css2?family=Open+Sans:wght@400;600&display=swap">
<style>
  :root {
    --ink: #000000;
    --paper: #ffffff;
    --backdrop: #e9e6e2;
    --emblem-tone: #1c1c1c;
    --emblem-light: #f2f2f2;
  }
  * { margin: 0; padding: 0; box-sizing: border-box; }
  html, body {
    width: 1200px; height: 900px; overflow: hidden;
    background: var(--backdrop);
    font-family: "Open Sans", Arial, sans-serif;
  }
  .stage { position: relative; width: 1200px; height: 900px; }

  .card {
    position: absolute;
    background: var(--paper);
    box-shadow: 0 6px 18px rgba(0,0,0,.18);
    overflow: hidden;
  }

  /* Front card */
  .card--front { left: 78px; top: 35px; width: 588px; height: 363px; }
  .front__head {
    height: 155px; display: flex; align-items: center; padding-left: 32px;
  }
  .brand-name {
    font-size: 50px; font-weight: 400; color: var(--ink); letter-spacing: .5px;
  }
  .front__body {
    position: absolute; left: 0; right: 0; top: 155px; bottom: 0;
    background: var(--ink); color: var(--paper);
    padding: 14px 0 0 32px;
  }
  .owners { font-size: 20px; font-weight: 600; margin-bottom: 18px; }
  .contact-list { list-style: none; }
  .contact-list li {
    display: flex; align-items: center; gap: 9px;
    font-size: 15.5px; line-height: 24.5px;
  }
  .contact-list svg { width: 13px; height: 13px; flex: none; fill: var(--paper); }
  .front__emblem {
    position: absolute; right: 10px; top: 6px; width: 178px; height: 196px;
    background: var(--emblem-tone);
  }

  /* Back card */
  .card--back { left: 388px; top: 505px; width: 567px; height: 352px; }
  .back__band {
    position: absolute; left: 0; right: 0; top: 85px; height: 181px;
    background: var(--ink); color: var(--paper);
  }
  .back__emblem {
    position: absolute; left: 245px; top: 13px; width: 76px; height: 76px;
    border: 2px solid var(--paper); background: var(--emblem-light);
  }
  .back__rule {
    position: absolute; left: 128px; width: 310px; height: 1px; background: var(--paper);
  }
  .back__rule--top { top: 85px; }
  .back__rule--bottom { top: 153px; }
  .back__name {
    position: absolute; left: 0; right: 0; top: 95px; text-align: center;
    font-size: 38px; font-weight: 400; letter-spacing: .5px;
  }
  .back__tagline {
    position: absolute; left: 0; right: 0; top: 158px; text-align: center;
    font-size: 7px; letter-spacing: .9px; text-transform: uppercase;
  }
</style>
</head>
<body>
<div class="stage">

  <section class="card card--front">
    <header class="front__head">
      <h1 class="brand-name">Lather and Lore</h1>
    </header>
    <div class="front__body">
      <h2 class="owners">Ross and Edith Carwell</h2>
      <ul class="contact-list">
        <li><svg viewBox="0 0 16 16"><path d="M3.6 1.2l2.3 2.3-1.3 2a9 9 0 0 0 5.9 5.9l2-1.3 2.3 2.3-1.6 2.2C6.8 16 0 9.2.4 2.8z"/></svg>0418529647</li>
        <li><svg viewBox="0 0 16 16"><path d="M1 3h14v10H1z" fill="none" stroke="#fff" stroke-width="1.5"/><path d="M1 3l7 6 7-6" fill="none" stroke="#fff" stroke-width="1.5"/></svg>ross@latherandlore.com.au</li>
        <li><svg viewBox="0 0 16 16"><path d="M1 3h14v10H1z" fill="none" stroke="#fff" stroke-width="1.5"/><path d="M1 3l7 6 7-6" fill="none" stroke="#fff" stroke-width="1.5"/></svg>edith@latherandlore.com.au</li>
        <li><svg viewBox="0 0 16 16"><path d="M1 3h14v10H1z" fill="none" stroke="#fff" stroke-width="1.5"/><path d="M1 3l7 6 7-6" fill="none" stroke="#fff" stroke-width="1.5"/></svg>sales@theblokesbalmery.com.au</li>
        <li><svg viewBox="0 0 16 16"><circle cx="8" cy="8" r="7"/><path d="M1 8h14M8 1c-3 3-3 11 0 14M8 1c3 3 3 11 0 14" fill="none" stroke="#000" stroke-width="1"/></svg>www.latherandlore.com.au</li>
      </ul>
      <div class="front__emblem" role="img" aria-label="Faint brand emblem decoration"></div>
    </div>
  </section>

  <section class="card card--back">
    <div class="back__band">
      <div class="back__emblem" role="img" aria-label="Brand emblem"></div>
      <div class="back__rule back__rule--top"></div>
      <h2 class="back__name">Lather and Lore</h2>
      <div class="back__rule back__rule--bottom"></div>
      <p class="back__tagline">Purveyors of gentlemen's stiffeners and grooming requisites</p>
    </div>
  </section>

</div>
</body>
</html>
```